business card for horse saddlery

after a new business card for our saddlery, i will add 2 logos we have previously used and they can be used (or not) . Any images can be used from our website also at www.brambletons.net.au, I have also added our brand logo, which may be good to incorporate on back ? we have over 15, 000 items online, ship Australia Wide.

Target Market(s)

horse owners

Industry/Entity Type

Retail - Equestrian

Contact Information for Business Card

Fairwick Horse Supplies, 1300 48 72 93, www.brambletons.net.au, 247 Dunmore Rd Wallaby Q 4587

Requirements
Must have
• ridegleam is our brand so ridegleam logo on back as 'distributers of', easy to read
Nice to have
• professional but fun
Should not have
• double sided (description wont save double sided)

```html
<!DOCTYPE html>
<html lang="en">
<head>
<meta charset="utf-8">
<title>Fairwick Horse Supplies – Business Card</title>
<link rel="stylesheet" href="https://fonts.googleapis.com/css2?family=Lato:wght@400;700&display=swap">
<style>
  :root {
    --backdrop: #2a2b2d;
    --card: #ffffff;
    --navy: #0b3a80;
    --sun: #fdb61b;
    --sun-soft: #fde3a4;
    --brand-blue: #1a4f8f;
  }
  * { box-sizing: border-box; margin: 0; padding: 0; }
  html, body { width: 1200px; height: 800px; overflow: hidden; }
  body {
    background: var(--backdrop);
    font-family: "Lato", Arial, sans-serif;
    display: flex;
    align-items: center;
    justify-content: center;
    gap: 40px;
  }
  .card {
    position: relative;
    width: 540px;
    height: 320px;
    background: var(--card);
    border-radius: 22px;
    overflow: hidden;
  }
  /* front */
  .hero-art {
    position: absolute;
    right: 0;
    top: 0;
    width: 320px;
    height: 320px;
  }
  .brand {
    position: absolute;
    left: 32px;
    top: 52px;
    display: flex;
    align-items: center;
    gap: 12px;
  }
  .brand-dot {
    width: 34px; height: 34px;
    border-radius: 50%;
    background: var(--sun);
  }
  .brand-name {
    color: var(--navy);
    font-weight: 700;
    font-size: 22px;
    line-height: 1.15;
  }
  .contact {
    position: absolute;
    left: 32px;
    bottom: 32px;
    list-style: none;
    display: grid;
    gap: 8px;
  }
  .contact li {
    display: flex;
    align-items: flex-start;
    gap: 10px;
    color: var(--navy);
    font-size: 14px;
    line-height: 1.25;
  }
  .contact .phone { font-weight: 700; font-size: 18px; }
  .contact svg { flex: none; width: 14px; height: 14px; margin-top: 2px; }
  /* back */
  .card-back {
    display: flex;
    align-items: center;
    justify-content: center;
    gap: 14px;
    padding-top: 20px;
  }
  .partner-mark {
    width: 18px; height: 18px;
    background: var(--brand-blue);
  }
  .partner-name {
    font-weight: 700;
    font-size: 52px;
    letter-spacing: 2px;
    color: var(--brand-blue);
    text-transform: uppercase;
  }
</style>
</head>
<body>
  <section class="card card-front">
    <svg class="hero-art" viewBox="0 0 320 320" role="img" aria-label="Illustration of a white horse head with a flowing blue mane set against a rising yellow sun">
      <defs>
        <linearGradient id="hero-tones" x1="0" y1="1" x2="1" y2="0">
          <stop offset="0" stop-color="var(--sun)"/>
          <stop offset="0.45" stop-color="var(--sun-soft)"/>
          <stop offset="0.75" stop-color="#ffffff"/>
          <stop offset="1" stop-color="var(--navy)"/>
        </linearGradient>
      </defs>
      <path d="M0 320 V120 A140 140 0 0 1 250 0 H320 V320 Z" fill="url(#hero-tones)"/>
    </svg>

    <div class="brand">
      <span class="brand-dot"></span>
      <span class="brand-name">Fairwick<br>Horse Supplies</span>
    </div>

    <ul class="contact">
      <li>
        <svg viewBox="0 0 14 14" aria-hidden="true"><path d="M7 1a4.5 4.5 0 0 0-4.5 4.5C2.5 9 7 13 7 13s4.5-4 4.5-7.5A4.5 4.5 0 0 0 7 1z" fill="var(--sun)"/><circle cx="7" cy="5.5" r="1.6" fill="#fff"/></svg>
        <span>247 Dunmore Rd<br>Wallaby Q 4587</span>
      </li>
      <li class="phone">
        <svg viewBox="0 0 14 14" aria-hidden="true"><path d="M3 1.5l2.2 2.6-1.2 1.6a8 8 0 0 0 4.3 4.3l1.6-1.2 2.6 2.2-1.4 1.8C6 12.5 1.5 8 1.2 2.9z" fill="var(--sun)"/></svg>
        <span>1300 48 72 93</span>
      </li>
      <li>
        <svg viewBox="0 0 14 14" aria-hidden="true"><rect x="1" y="3" width="12" height="8" rx="1" fill="var(--sun)"/><path d="M1.5 3.5L7 8l5.5-4.5" stroke="#fff" fill="none"/></svg>
        <span>office@brambletons.net.au</span>
      </li>
      <li>
        <svg viewBox="0 0 14 14" aria-hidden="true"><circle cx="7" cy="7" r="6" fill="var(--sun)"/><path d="M1 7h12M7 1c-2.5 3-2.5 9 0 12M7 1c2.5 3 2.5 9 0 12" stroke="#fff" stroke-width="0.9" fill="none"/></svg>
        <span>brambletons.net.au</span>
      </li>
    </ul>
  </section>

  <section class="card card-back">
    <span class="partner-mark"></span>
    <span class="partner-name">Ridegleam</span>
  </section>
</body>
</html>
```